verdant terraces simple classy business card design

my name is owen harlow and I run a gardening business aimed at high class verdant terraces. the business name is verdant terraces and our logo was designed on pixel forum .My clientel are anything from residential homes to businesses. I take pride in my work and know that I offer a service like no other in my area.
The business card will be used to represent my business and I want it to be not only rememberable, but simplistic and modern. Eye catching too. Of course I would like it relatable to gardening and appealing to the correct clientel - those being garden enthusiasts, prestigious homes and businesses that are after top of the line gardening services like no other on the market.
I am not a typical lawn mowing business so I don't want a typical card design that represents that. The gardens I work with are generally million dollar properties with owners who are very garden proud looking for upkeep and guidance from me along with sometimes whole new garden designs. I want the business cards to show to my clients that I take pride, as they do, in their garden. And I want them to know from my card that I am a professional, qualified horticulturist offering them a top of the line service for life. I want them to refer my business on. I want them to look at my business card and see class and professionalism in a modern unique bold way.
The card should be simple with the possibility of the logo on the front being embossed/debossed and my details on the back the card should have a organic garden feel it's very important to me that it is absolutely perfect
I am also very open to ideas and suggestions so look forward to seeing the designs. the business logo has been supplied with this project and I want the card to be double sided

Contact info is
Owen Harlow - Managing Director / Horticulturist
Phone : 0481 526 704
Email: owenharlow@verdantterraces.com.au

Target Market(s)

high class gardens residential and commercial

Industry/Entity Type

Gardener

Contact Information for Business Card

Contact info is
Phone : 0481 526 704

PLEASE MAKE CARD DOUBLE SIDED

Requirements
Must have
• organic simple classy modern feel
• must flow with the current logo that has been supplied with this project
• Double sided
• Must explain in a simple way that I deal with high end gardens and I'm a qualified horticulturist
Nice to have
• embossed debossed logo
Should not have
• shouldn't be to busy or cheap looking

```html
<!DOCTYPE html>
<html lang="en">
<head>
<meta charset="utf-8">
<title>Verdant Terraces — Business Card</title>
<link rel="stylesheet" href="https://fonts.googleapis.com/css2?family=Tinos:wght@400&display=swap">
<style>
  :root {
    --backdrop: #e9e5de;
    --card: #4a4b4e;
    --leaf: #3f9a50;
    --ink-light: #e6e6e6;
    --shadow: rgba(0, 0, 0, 0.22);
  }
  * { box-sizing: border-box; margin: 0; padding: 0; }
  html, body {
    width: 1200px;
    height: 413px;
    overflow: hidden;
    background: var(--backdrop);
    font-family: "Tinos", "Times New Roman", serif;
  }
  .card-set {
    display: flex;
    gap: 40px;
    padding: 52px 40px;
    width: 1200px;
    height: 413px;
  }
  .card {
    position: relative;
    width: 540px;
    height: 309px;
    background: var(--card);
    overflow: hidden;
    box-shadow: 0 6px 18px var(--shadow);
  }

  /* Front */
  .card--front {
    display: flex;
    flex-direction: column;
    align-items: center;
    justify-content: center;
    gap: 18px;
  }
  .brand-mark {
    width: 74px;
    height: 74px;
    border-radius: 50%;
    background: var(--leaf);
  }
  .brand-name {
    color: var(--leaf);
    font-weight: 400;
    font-size: 34px;
    letter-spacing: 0.12em;
    text-transform: uppercase;
    text-align: center;
    line-height: 1.1;
  }

  /* Back */
  .card--back { padding: 28px 30px; }
  .holder-name {
    color: var(--leaf);
    font-size: 17px;
    letter-spacing: 0.04em;
    text-transform: uppercase;
    font-weight: 400;
  }
  .holder-role {
    color: var(--ink-light);
    font-size: 9.5px;
    margin-top: 6px;
  }
  .contact {
    position: absolute;
    left: 30px;
    bottom: 26px;
    list-style: none;
    color: var(--leaf);
    font-size: 12px;
    line-height: 1.75;
  }
  .side-mark {
    position: absolute;
    right: -70px;
    top: 60px;
    width: 170px;
    height: 170px;
    border-radius: 50%;
    background: var(--leaf);
  }
</style>
</head>
<body>
  <main class="card-set">
    <section class="card card--front" aria-label="Card front">
      <div class="brand-mark" aria-hidden="true"></div>
      <h1 class="brand-name">Verdant Terraces</h1>
    </section>

    <section class="card card--back" aria-label="Card back">
      <h2 class="holder-name">Owen Harlow</h2>
      <p class="holder-role">Managing Director / Horticulturist</p>
      <ul class="contact">
        <li class="contact__phone">0481 526 704</li>
        <li class="contact__email">owenharlow@verdantterraces.com.au</li>
      </ul>
      <div class="side-mark" aria-hidden="true"></div>
    </section>
  </main>
</body>
</html>
```